Keystone Haulers Billboard design

I need two billboard designs using our logo and adding a few words Looking for a black background with our logo and wording in either purple or white.

need it to have our website keystonehaulers-example.com. phone number 555 201 4387

Also have 16/20/30 yard dumpsters available!

one billboard is size 7x21 feet the other is 15x 21 ft

Target Market(s)

Contractors, home owners

Requirements
Must have
• Use font similar to logo that is eye catching

```html
<!DOCTYPE html>
<html lang="en">
<head>
<meta charset="utf-8">
<title>Keystone Haulers Billboards</title>
<link rel="stylesheet" href="https://fonts.googleapis.com/css2?family=Exo+2:wght@500;600;700;800&display=swap">
<style>
  :root {
    --purple: #7b3aa6;
    --purple-deep: #4a1f66;
    --black: #0d0a10;
    --white: #ffffff;
    --stage: #b5b5b5;
  }
  * { box-sizing: border-box; margin: 0; padding: 0; }
  html, body { width: 984px; height: 1200px; overflow: hidden; }
  body {
    background: var(--stage);
    font-family: "Exo 2", "Arial Narrow", sans-serif;
    position: relative;
  }
  .board { position: absolute; overflow: hidden; background: var(--black); }
  .photo {
    position: absolute; inset: 0;
    background: linear-gradient(125deg, var(--purple) 0%, var(--purple) 22%, var(--black) 48%, #1a0f22 70%, var(--purple-deep) 100%);
  }
  .tear { position: absolute; left: 0; width: 100%; }
  .brand {
    position: absolute; color: var(--white); font-weight: 800;
    text-transform: uppercase; line-height: 0.95; letter-spacing: 1px;
  }
  .headline {
    position: absolute; color: var(--white); font-weight: 700;
    text-transform: uppercase; line-height: 0.95; letter-spacing: 0.5px;
  }
  .sizes { position: absolute; display: flex; align-items: flex-start; color: var(--white); }
  .size { display: flex; flex-direction: column; align-items: center; }
  .size b { font-weight: 800; line-height: 0.9; }
  .size span { font-weight: 700; line-height: 1; }
  .slash { background: var(--white); opacity: 0.8; transform: skewX(-18deg); width: 1.5px; align-self: stretch; }
  .cta { position: absolute; color: var(--white); text-align: center; }
  .cta small { display: block; font-weight: 600; text-transform: uppercase; }
  .cta .pill {
    display: block; border: 2px solid var(--white); border-radius: 999px;
    font-weight: 600; text-transform: uppercase; letter-spacing: 0.5px;
  }
  .contact { position: absolute; display: flex; align-items: center; color: var(--purple); font-weight: 700; }
  .contact .icon { flex: none; }
  .arrow { position: absolute; }

  /* wide billboard 7 x 21 ft */
  .board--wide { left: 42px; top: 30px; width: 900px; height: 300px; }
  .board--wide .photo { bottom: 90px; }
  .board--wide .tear { top: 180px; height: 120px; }
  .board--wide .brand { left: 56px; top: 44px; font-size: 34px; }
  .board--wide .headline { left: 355px; top: 42px; font-size: 32px; }
  .board--wide .sizes { left: 350px; top: 128px; gap: 12px; }
  .board--wide .size b { font-size: 46px; }
  .board--wide .size span { font-size: 23px; }
  .board--wide .cta { left: 631px; top: 136px; width: 235px; }
  .board--wide .cta small { font-size: 12px; margin-bottom: 6px; }
  .board--wide .cta .pill { font-size: 21px; padding: 3px 0; }
  .board--wide .arrow { left: 808px; top: 208px; }
  .board--wide .contact--phone { left: 50px; top: 235px; font-size: 38px; gap: 10px; }
  .board--wide .contact--web { left: 405px; top: 246px; font-size: 21px; gap: 8px; }

  /* tall billboard 15 x 21 ft */
  .board--tall { left: 206px; top: 362px; width: 572px; height: 800px; }
  .board--tall .photo { bottom: 200px; }
  .board--tall .tear { top: 530px; height: 270px; }
  .board--tall .brand { left: 80px; top: 48px; font-size: 44px; }
  .board--tall .headline { left: 76px; top: 168px; font-size: 54px; line-height: 0.92; }
  .board--tall .sizes { left: 74px; top: 388px; gap: 12px; }
  .board--tall .size b { font-size: 52px; }
  .board--tall .size span { font-size: 26px; }
  .board--tall .cta { left: 76px; top: 482px; width: 240px; }
  .board--tall .cta small { font-size: 13px; margin-bottom: 5px; }
  .board--tall .cta .pill { font-size: 23px; padding: 3px 0; }
  .board--tall .arrow { left: 222px; top: 548px; }
  .board--tall .contact--phone { left: 68px; top: 664px; font-size: 54px; gap: 12px; }
  .board--tall .contact--web { left: 70px; top: 740px; font-size: 27px; gap: 10px; }
</style>
</head>
<body>

<!-- Wide billboard -->
<section class="board board--wide">
  <div class="photo" role="img" aria-label="Purple and black duotone photo of a roll-off dumpster truck"></div>
  <svg class="tear" viewBox="0 0 900 120" preserveAspectRatio="none" aria-hidden="true">
    <path d="M0 30 L40 18 L80 28 L120 14 L170 24 L210 10 L250 26 L300 20 L330 34 L380 40 L420 48 L460 42 L520 52 L570 46 L610 40 L660 24 L700 30 L740 14 L790 22 L840 8 L900 16 L900 120 L0 120 Z" fill="#ffffff"/>
  </svg>
  <div class="brand">Keystone<br>Haulers</div>
  <h2 class="headline">Residential &amp; Commercial<br>Dumpster Rentals</h2>
  <div class="sizes">
    <div class="size"><b>16</b><span>yard</span></div>
    <i class="slash"></i>
    <div class="size"><b>20</b><span>yard</span></div>
    <i class="slash"></i>
    <div class="size"><b>30</b><span>yard</span></div>
  </div>
  <div class="cta"><small>Rent your dumpster today</small><span class="pill">Book now at</span></div>
  <svg class="arrow" width="50" height="58" viewBox="0 0 50 58" aria-hidden="true">
    <path d="M30 4 C46 16 42 44 10 48" fill="none" stroke="var(--purple)" stroke-width="3" stroke-linecap="round"/>
    <path d="M18 40 L8 48 L19 55" fill="none" stroke="var(--purple)" stroke-width="3" stroke-linecap="round" stroke-linejoin="round"/>
  </svg>
  <div class="contact contact--phone">
    <svg class="icon" width="34" height="34" viewBox="0 0 34 34" aria-hidden="true">
      <circle cx="17" cy="17" r="16" fill="var(--purple)"/>
      <path d="M11 9 L14 9 L15.5 13 L13.5 14.5 C14.5 17 16.5 19.5 19.5 20.5 L21 18.5 L25 20 L25 23 C25 24 24 25 23 25 C15.5 24.5 9.5 18.5 9 11 C9 10 10 9 11 9 Z" fill="#fff"/>
    </svg>
    555 201 4387
  </div>
  <div class="contact contact--web">
    <svg class="icon" width="24" height="24" viewBox="0 0 24 24" aria-hidden="true">
      <circle cx="12" cy="12" r="11.5" fill="var(--purple)"/>
      <g fill="none" stroke="#fff" stroke-width="1.3">
        <circle cx="12" cy="12" r="7"/><ellipse cx="12" cy="12" rx="3" ry="7"/>
        <line x1="5" y1="12" x2="19" y2="12"/><line x1="6" y1="8.5" x2="18" y2="8.5"/><line x1="6" y1="15.5" x2="18" y2="15.5"/>
      </g>
    </svg>
    KEYSTONEHAULERS-EXAMPLE.COM
  </div>
</section>

<!-- Tall billboard -->
<section class="board board--tall">
  <div class="photo" role="img" aria-label="Purple and black duotone close-up photo of a dumpster on a roll-off truck"></div>
  <svg class="tear" viewBox="0 0 572 270" preserveAspectRatio="none" aria-hidden="true">
    <path d="M0 10 L20 40 L40 70 L60 96 L90 104 L120 90 L150 110 L180 96 L200 70 L215 100 L240 112 L265 96 L290 116 L320 100 L350 84 L380 96 L410 70 L440 56 L470 40 L500 30 L530 22 L572 8 L572 270 L0 270 Z" fill="#ffffff"/>
  </svg>
  <div class="brand">Keystone<br>Haulers</div>
  <h2 class="headline">Residential &amp;<br>Commercial<br>Dumpster<br>Rentals</h2>
  <div class="sizes">
    <div class="size"><b>16</b><span>yard</span></div>
    <i class="slash"></i>
    <div class="size"><b>20</b><span>yard</span></div>
    <i class="slash"></i>
    <div class="size"><b>30</b><span>yard</span></div>
  </div>
  <div class="cta"><small>Rent your dumpster today</small><span class="pill">Book now at</span></div>
  <svg class="arrow" width="60" height="92" viewBox="0 0 60 92" aria-hidden="true">
    <path d="M18 4 C52 20 50 66 20 84" fill="none" stroke="#fff" stroke-width="3.5" stroke-linecap="round"/>
    <path d="M18 68 L18 86 L34 84" fill="none" stroke="#fff" stroke-width="3.5" stroke-linecap="round" stroke-linejoin="round"/>
  </svg>
  <div class="contact contact--phone">
    <svg class="icon" width="46" height="46" viewBox="0 0 34 34" aria-hidden="true">
      <circle cx="17" cy="17" r="16" fill="var(--purple)"/>
      <path d="M11 9 L14 9 L15.5 13 L13.5 14.5 C14.5 17 16.5 19.5 19.5 20.5 L21 18.5 L25 20 L25 23 C25 24 24 25 23 25 C15.5 24.5 9.5 18.5 9 11 C9 10 10 9 11 9 Z" fill="#fff"/>
    </svg>
    555 201 4387
  </div>
  <div class="contact contact--web">
    <svg class="icon" width="30" height="30" viewBox="0 0 24 24" aria-hidden="true">
      <circle cx="12" cy="12" r="11.5" fill="var(--purple)"/>
      <g fill="none" stroke="#fff" stroke-width="1.3">
        <circle cx="12" cy="12" r="7"/><ellipse cx="12" cy="12" rx="3" ry="7"/>
        <line x1="5" y1="12" x2="19" y2="12"/><line x1="6" y1="8.5" x2="18" y2="8.5"/><line x1="6" y1="15.5" x2="18" y2="15.5"/>
      </g>
    </svg>
    KEYSTONEHAULERS-EXAMPLE.COM
  </div>
</section>

</body>
</html>
```